Digital One Pager for Consulting Practice

I would like the essence of the content in my ppt consolidated into a one-pager. The one-pager will mainly be sent via email as a pdf and intended to excite and invite new clients and establish the credibility of my boutique high-end consulting firm. Infographics and symbols would be a plus. The target client should view the firm as providing premeir service. The client is getting a thought partner.

Target Market(s)

Large Medical Device Manufacturer Executives, Early-Stage Medical Device Manufacturer Executives, Partners at VC Firms

Industry/Entity Type

Medical Equipment

Colors
0355a3
f37122

Requirements
Must have
• Please match the color scheme in ppt. Please use the existing logo. I am very open to better graphics on the process. My photo does not need to be on the digital flyer. Hyper link to the website and email is needed.
Nice to have
• Infographics

```html
<!DOCTYPE html>
<html lang="en">
<head>
<meta charset="utf-8">
<title>Harlow Advisory — One Pager</title>
<link rel="stylesheet" href="https://fonts.googleapis.com/css2?family=Jost:wght@400;500;600&family=Lora:wght@400;500&display=swap">
<style>
  :root {
    --navy: #0d1834;
    --navy-soft: #1b2a4e;
    --orange: #e8452a;
    --grey: #8b9099;
    --paper: #f3f3f4;
    --white: #ffffff;
    --ink: #1c2238;
    --backdrop: #dde3e5;
  }
  * { box-sizing: border-box; margin: 0; padding: 0; }
  html, body { width: 1200px; height: 890px; overflow: hidden; }
  body { background: var(--backdrop); font-family: "Jost", sans-serif; color: var(--ink); }

  .flyer {
    position: absolute; left: 256px; top: 0;
    width: 688px; height: 890px;
    background: var(--navy); overflow: hidden;
  }
  .hero-photo {
    position: absolute; left: 0; top: 0; width: 688px; height: 312px;
    background: linear-gradient(135deg, #24355c 0%, #142244 45%, #0d1834 100%);
  }
  .hero-shapes { position: absolute; left: 0; top: 0; }

  .brand {
    position: absolute; top: 38px; right: 40px;
    display: flex; align-items: center; gap: 8px;
    font-family: "Jost", sans-serif; font-weight: 600; font-size: 17px;
    letter-spacing: 2px; color: var(--navy);
  }
  .brand-dot { width: 12px; height: 12px; border-radius: 50%; background: var(--navy); }

  .hero-title { position: absolute; left: 36px; top: 196px; color: var(--white); }
  .hero-kicker { font-size: 15px; letter-spacing: 4px; color: var(--orange); font-weight: 500; }
  .hero-word { font-family: "Lora", serif; font-size: 58px; line-height: 1; font-weight: 500; }

  .left-col {
    position: absolute; left: 0; top: 312px; width: 330px; height: 578px;
    background: var(--paper); padding: 26px 30px 0 36px;
  }
  .right-col {
    position: absolute; left: 330px; top: 246px; width: 358px; height: 644px;
    padding: 22px 34px 0 34px; color: var(--white);
  }
  .section-title {
    font-family: "Lora", serif; font-weight: 400; font-size: 24px;
    padding-bottom: 8px; border-bottom: 1px solid #c9ccd2; margin-bottom: 14px;
  }
  .right-col .section-title { border-bottom-color: #3a4668; }

  .tick-list { list-style: none; }
  .tick-list li {
    position: relative; padding-left: 20px; margin-bottom: 11px;
    font-size: 9.5px; line-height: 1.35;
  }
  .tick-list li::before {
    content: "✓"; position: absolute; left: 0; top: 0;
    width: 12px; height: 12px; border-radius: 50%;
    background: var(--orange); color: var(--white);
    font-size: 8px; line-height: 12px; text-align: center;
  }
  .item-head { font-weight: 600; letter-spacing: .6px; text-transform: uppercase; }
  .item-sub { color: #5a6072; }
  .right-col .item-sub { color: #c4c9d6; }

  .service { display: flex; gap: 10px; margin-bottom: 10px; font-size: 9.5px; line-height: 1.4; }
  .service-icon { flex: 0 0 16px; }
  .service ul { list-style: none; color: #5a6072; }
  .service li::before { content: "• "; color: var(--ink); }

  .partners { display: flex; gap: 18px; align-items: center; margin-top: 4px; }
  .partner-badge { width: 110px; height: 34px; background: #d7d9de; border-radius: 3px; }

  .process { display: block; margin: 0 0 10px 20px; }
  .contact-label { font-size: 9px; letter-spacing: 2px; color: var(--orange); font-weight: 600; margin-bottom: 6px; }
  .contact-line { font-family: "Lora", serif; font-size: 15px; line-height: 1.45; }
  .contact-line a { color: var(--white); text-decoration: none; }
  .spaced { margin-top: 22px; }
  .right-col .spaced { margin-top: 18px; }
</style>
</head>
<body>
<main class="flyer">
  <div class="hero-photo" role="img" aria-label="Photo of a consultant's hands working at a desk in dark blue tones"></div>

  <svg class="hero-shapes" width="688" height="320" viewBox="0 0 688 320" aria-hidden="true">
    <path d="M360 0 H688 V118 C590 134 470 110 360 0 Z" fill="var(--white)"/>
    <path d="M0 308 H230 C300 308 330 240 400 200 C480 155 580 130 688 118" fill="none" stroke="var(--orange)" stroke-width="8"/>
  </svg>

  <div class="brand"><span class="brand-dot"></span>HARLOW ADVISORY</div>

  <header class="hero-title">
    <p class="hero-kicker">HARLOW ADVISORY</p>
    <h1 class="hero-word">Value.</h1>
  </header>

  <section class="left-col">
    <h2 class="section-title">Experience</h2>
    <ul class="tick-list">
      <li><span class="item-head">Over a decade @FDA</span><br><span class="item-sub">(Former Deputy Division Director)</span></li>
      <li><span class="item-head">Expertise:</span> <span class="item-sub">Cardiovascular, Ophthalmology, General Hospital, Infection Control, Dental, Anesthesia, Respiratory</span></li>
      <li><span class="item-head">Vice President Regulatory Affairs / Quality Assurance @Meridian (Fortune 100 Company)</span><br>
        <span class="item-sub">· Initiated reorganization of department<br>· Led major compliance effort<br>· Successful FDA inspection (no observations)</span></li>
    </ul>

    <h2 class="section-title spaced">Services</h2>
    <div class="service">
      <svg class="service-icon" width="16" height="14" viewBox="0 0 16 14" aria-hidden="true"><path d="M1 13H15M3 12V7M7 12V3M11 12V6" stroke="var(--orange)" stroke-width="2" fill="none"/></svg>
      <div><p class="item-head">Regulatory Strategy</p><ul><li>RAQA Organizational Structure</li><li>Regulatory Pathway</li></ul></div>
    </div>
    <div class="service">
      <svg class="service-icon" width="16" height="14" viewBox="0 0 16 14" aria-hidden="true"><rect x="1" y="2" width="14" height="9" rx="2" fill="var(--orange)"/></svg>
      <div><p class="item-head">FDA Communications</p><ul><li>Deficiency Response</li><li>Application Review</li></ul></div>
    </div>
    <div class="service">
      <svg class="service-icon" width="16" height="14" viewBox="0 0 16 14" aria-hidden="true"><circle cx="8" cy="5" r="3" fill="var(--orange)"/><path d="M2 13C2 9 14 9 14 13Z" fill="var(--orange)"/></svg>
      <div><p class="item-head">Interim Executive Leadership</p><ul><li>Compliance Remediation</li><li>Product Registration</li></ul></div>
    </div>

    <h2 class="section-title spaced">Network</h2>
    <div class="partners">
      <div class="partner-badge"></div>
      <div class="partner-badge"></div>
    </div>
  </section>

  <section class="right-col">
    <h2 class="section-title">Experience to Provide</h2>
    <ul class="tick-list">
      <li><span class="item-head">Executive Application Review</span><br><span class="item-sub">· Examples include Presubmission, IDE, 510(k), 513(g), PMA, Refuse to Accept, Hold letter<br>· Troubleshooting</span></li>
      <li><span class="item-head">Strategic Advice &amp; Diligence to Investors</span><br><span class="item-sub">· Validate &amp; Verify Founder Milestones<br>· Diligence portfolio company Regulatory and Quality systems</span></li>
    </ul>

    <h2 class="section-title spaced">Efficient Process</h2>
    <svg class="process" width="260" height="200" viewBox="0 0 260 200" role="img" aria-label="Four step process: exploratory call, regulatory landscape, problem statement, review and align on deliverables">
      <g font-family="Jost, sans-serif" fill="var(--white)">
        <path d="M60 40 C30 40 30 86 60 86 H170 C200 86 200 132 170 132 H60 C30 132 30 178 60 178" fill="none" stroke="var(--grey)" stroke-width="4"/>
        <rect x="40" y="22" width="150" height="36" rx="18" fill="var(--orange)"/>
        <text x="56" y="46" font-size="16" font-weight="600">01</text>
        <text x="92" y="37" font-size="8">Exploratory</text><text x="92" y="47" font-size="8">Call</text>
        <circle cx="170" cy="40" r="13" fill="var(--white)"/>
        <rect x="163" y="35" width="14" height="9" rx="2" fill="var(--orange)"/>

        <rect x="40" y="68" width="150" height="36" rx="18" fill="var(--grey)"/>
        <text x="160" y="92" font-size="16" font-weight="600">02</text>
        <text x="88" y="83" font-size="8">Regulatory</text><text x="88" y="93" font-size="8">Landscape</text>
        <circle cx="60" cy="86" r="13" fill="var(--white)"/>
        <rect x="53" y="81" width="14" height="10" fill="none" stroke="var(--grey)" stroke-width="1.5"/>
        <path d="M53 81 L60 87 L67 81" fill="none" stroke="var(--grey)" stroke-width="1.5"/>

        <rect x="40" y="114" width="150" height="36" rx="18" fill="var(--orange)"/>
        <text x="56" y="138" font-size="16" font-weight="600">03</text>
        <text x="92" y="129" font-size="8">Problem</text><text x="92" y="139" font-size="8">Statement</text>
        <circle cx="170" cy="132" r="13" fill="var(--white)"/>
        <rect x="164" y="125" width="12" height="15" fill="none" stroke="var(--orange)" stroke-width="1.5"/>
        <path d="M167 130H173M167 134H173" stroke="var(--orange)" stroke-width="1.2"/>

        <rect x="40" y="160" width="150" height="36" rx="18" fill="var(--grey)"/>
        <text x="160" y="184" font-size="16" font-weight="600">04</text>
        <text x="82" y="175" font-size="8">Review &amp; Align</text><text x="82" y="185" font-size="8">on Deliverables</text>
        <circle cx="60" cy="178" r="13" fill="var(--white)"/>
        <path d="M60 186 C54 179 54 176 54 174 A6 6 0 0 1 66 174 C66 176 66 179 60 186Z" fill="var(--grey)"/>
        <circle cx="60" cy="174" r="2" fill="var(--white)"/>
      </g>
    </svg>

    <h2 class="section-title">Let's Chat</h2>
    <p class="contact-label">CONTACT</p>
    <p class="contact-line"><a href="tel:+12025550148">+1.202.555.0148</a></p>
    <p class="contact-line"><a href="mailto:info@harlowadvisory.com">info@harlowadvisory.com</a></p>
    <p class="contact-line"><a href="https://harlowadvisory.com">harlowadvisory.com</a></p>
  </section>
</main>
</body>
</html>
```